Personal Brand (Influencer) Website

I'm looking for a brand new website design for a youtuber/influencer Dane Whitfield.

I'm looking for a sleek design that is visually appealing while still maintaining full functionality and user experience.

Here is our current website: http://danewhitfieldhq.example/

I want to combine some of the best elements and designs from the following websites.

https://www.milosparkwater.example/
https://www.renakurov.example/
https://otisbramley.example/
https://www.feliximarsh.example/
http://danewhitfieldhq.example/
http://www.quinvel.example/

Here are the different tabs that I would need designed as well as the main page:

Home Page (main page)
Blogs
My story (about me)
Top 100 book list
Contact

Here are several links and social media handles for you to get a better gauge on the branding of Dane Whitfield:
https://www.vidstreamhub.example/channel/XQpaer4k2z-M7ttPPw_HNd5q
https://rapid-ascent.example/market-blog/uncategorized/dane-whitfield-entrepreneur-winning-market-follow-data-ep-17/
https://danelisten2.pagerunner.example/optin-48203917
https://www.photoshare.example/officialdanewhitfield/

```html
<!DOCTYPE html>
<html lang="en">
<head>
<meta charset="utf-8">
<title>Dane Whitfield</title>
<link rel="stylesheet" href="https://fonts.googleapis.com/css2?family=Alegreya:ital,wght@0,400;0,700;0,800;1,400&display=swap">
<style>
:root{
  --teal:#58b39b;
  --teal-deep:#1f8c8a;
  --olive:#9aa21a;
  --ink:#1c1c1c;
  --grey:#8a8a8a;
  --navy:#13163a;
  --card:#33344a;
  --purple:#4b2c8a;
  --footer:#1f1f23;
  --white:#ffffff;
}
*{margin:0;padding:0;box-sizing:border-box}
html,body{width:1200px;height:3789px;overflow:hidden}
body{position:relative;background:var(--white);font-family:"Alegreya",Georgia,serif;color:var(--ink)}
.abs{position:absolute}

/* hero */
.hero{left:0;top:0;width:1200px;height:813px;background:linear-gradient(180deg,#7d7466 0%,#b8a585 35%,#9c8458 62%,#5c4c30 100%)}
.hero-person{left:0;top:110px;width:470px;height:703px;background:radial-gradient(ellipse at 40% 40%,#d9b398 0%,#7a6048 55%,rgba(60,45,30,0) 75%)}
.brand{left:30px;top:22px;color:var(--white);font-size:36px;line-height:1;font-weight:400}
.nav{right:62px;top:30px;display:flex;gap:26px;align-items:center}
.nav a{color:var(--white);text-decoration:none;font-size:20px;text-transform:uppercase}
.hero-name{left:480px;top:320px;color:var(--white);font-size:110px;line-height:1.05;font-weight:400}
.hero-name span{display:block}
.hero-name span+span{padding-left:90px}
.hero-bar{left:0;top:738px;width:1200px;height:75px;background:rgba(40,32,24,.72)}
.hero-bar p{position:absolute;left:525px;top:14px;color:var(--white);font-size:42px;letter-spacing:1px}

/* free course */
.offer{left:0;top:813px;width:1200px;height:728px;background:linear-gradient(180deg,#1c7f82 0%,#2aa29e 40%,#2e6a80 65%,#463a6a 82%,#c07a4a 92%,#2a2040 100%)}
.offer-figure{left:1040px;top:870px;width:90px;height:380px;background:linear-gradient(180deg,rgba(20,30,40,.35),rgba(20,30,40,.7))}
.offer-title{left:0;width:1212px;top:895px;text-align:center;color:var(--white);font-weight:400;font-size:58px;line-height:82px}
.btn-signup{left:482px;top:1091px;width:233px;height:46px;background:#131a2e;color:var(--white);font-size:20px;text-align:center;line-height:46px;text-transform:uppercase;letter-spacing:1px}
.promo{top:1187px;width:336px;height:316px;display:flex;align-items:center;justify-content:center;text-align:center;color:var(--white);font-size:40px;line-height:52px;padding:0 20px}
.promo-meet{left:68px;background:linear-gradient(160deg,#c9c9c9,#4b4b55)}
.promo-opp{left:430px;background:linear-gradient(160deg,#2f7f4a,#7ab5d6 60%,#3a9ac8)}
.promo-course{left:793px;background:linear-gradient(180deg,#3a3670,#a0457a 60%,#2c2550)}

/* about */
.avatar{left:70px;top:1578px;width:304px;height:304px;border-radius:50%;background:radial-gradient(circle at 50% 45%,#f0c8b0 0%,#2ec5e6 45%,#1fb0d6 100%);border:8px solid var(--white);box-shadow:0 0 0 2px #d8d8d8}
.bio-box{left:68px;top:1733px;width:531px;height:447px;background:var(--teal)}
.trophy{left:440px;top:1768px}
.bio-box-text{left:83px;top:1905px;width:505px;color:var(--white);font-size:19.5px;line-height:28px}
.bio-box-text p+p{margin-top:28px}
.stat{left:640px;top:1560px;width:450px;text-align:center}
.stat h2{color:var(--olive);font-size:64px;font-weight:800;line-height:1.1}
.stat h3{font-size:32px;font-weight:700;line-height:1.1}
.stat hr{width:60px;margin:14px auto 12px;border:0;border-top:1px solid #cfcfcf}
.stat p{color:var(--grey);font-size:19px;line-height:26px}
.join-sellers{left:599px;top:1793px;width:530px;height:387px;background:linear-gradient(180deg,#6f7480 0%,#9aa3ad 45%,#4b5560 75%,#6a4d7a 100%)}
.join-sellers p{position:absolute;left:0;top:62px;width:530px;text-align:center;color:var(--white);font-size:58px;line-height:72px}

/* posts */
.posts-title{left:0;width:1212px;top:2208px;text-align:center;color:var(--olive);font-size:54px;font-weight:800}
.posts-sub{left:0;width:1212px;top:2284px;text-align:center;color:var(--grey);font-size:19px}
.video{width:336px;overflow:hidden;background:linear-gradient(135deg,#1d1d3a,#3a2a60 55%,#111)}
.video.green{background:linear-gradient(135deg,#0d0d0d,#234a14 45%,#3a6ec8)}
.video.yellow{background:linear-gradient(135deg,#5aa0d8,#2a2a2a 50%,#e8d21a)}
.video .title{position:absolute;left:12px;top:10px;right:12px;color:var(--white);font-size:16px;white-space:nowrap;overflow:hidden;text-overflow:ellipsis}
.video .play{position:absolute;left:138px;top:50%;margin-top:-30px;width:60px;height:60px;border-radius:50%;background:rgba(0,0,0,.65)}
.video .play::after{content:"";position:absolute;left:24px;top:18px;border-left:18px solid var(--white);border-top:12px solid transparent;border-bottom:12px solid transparent}
.row1{top:2339px;height:197px}
.row2{top:2564px;height:187px}
.c1{left:68px}.c2{left:432px}.c3{left:800px}

/* testimonials */
.testi-bg{left:0;top:2780px;width:1200px;height:605px;background:radial-gradient(ellipse at 75% 35%,#bdbdbd 0%,#e6e6e6 35%,#ffffff 70%)}
.testi-title{left:680px;top:2800px;width:440px;text-align:center;color:#4a4a4a;font-size:58px;font-weight:800}
.testi-lead{left:660px;top:2870px;width:480px;text-align:center;font-size:23px;line-height:30px}
.quote{background:var(--card);color:var(--white)}
.quote .face{position:absolute;left:36px;top:40px;width:100px;height:100px;border-radius:50%;border:4px solid var(--white)}
.quote blockquote{position:absolute;left:170px;right:30px;top:38px;font-style:italic;font-size:19px;line-height:26px;color:#e8e8ee}
.quote cite{position:absolute;left:170px;bottom:30px;font-style:normal;font-size:15px;color:#b5b5c5}
.q1{left:68px;top:2809px;width:564px;height:217px}
.q2{left:632px;top:2998px;width:497px;height:175px}
.q3{left:68px;top:3178px;width:564px;height:182px}
.face-a{background:linear-gradient(135deg,#e8b23a,#6a5a4a)}
.face-b{background:linear-gradient(135deg,#e0b0b8,#8a5050)}
.face-c{background:linear-gradient(135deg,#8aa0b0,#4a3a30)}

/* community */
.community{left:0;top:3393px;width:1200px;height:86px;background:var(--navy)}
.community p{position:absolute;left:70px;top:20px;color:var(--white);font-size:33px;font-weight:700}
.btn-join{position:absolute;left:978px;top:22px;width:151px;height:41px;background:var(--purple);color:var(--white);font-size:20px;font-weight:700;text-align:center;line-height:41px}

/* footer */
.footer{left:0;top:3479px;width:1200px;height:310px;background:linear-gradient(180deg,#2a2a2f,var(--footer) 40%,#18181b)}
.footer-brand{left:100px;top:3555px;color:#d6d6d6;font-size:44px;line-height:1}
.footer-col h4{color:#cfcfcf;font-size:17px;font-weight:700;margin-bottom:16px}
.footer-col{top:3506px;color:#8a8a8f;font-size:13px;line-height:19px}
.footer-col p+p{margin-top:12px}
.col-about{left:442px;width:210px}
.col-contact{left:687px;width:230px}
.col-follow{left:993px;width:150px}
.social{display:flex;gap:10px}
.social span{width:26px;height:26px;background:#cfcfcf;border-radius:3px}
.copyright{left:0;width:1200px;top:3758px;text-align:center;color:#77777c;font-size:12px}
</style>
</head>
<body>

<section class="abs hero" role="img" aria-label="Photo of Dane Whitfield smiling in a cap with a backpack, mountain valley behind him"></section>
<div class="abs hero-person" role="img" aria-label="Dane Whitfield portrait"></div>
<div class="abs brand">Dane Whitfield</div>
<nav class="abs nav">
  <a href="#">Home</a><a href="#">About</a><a href="#">Resources</a><a href="#">Contact</a>
  <svg width="20" height="20" viewBox="0 0 20 20" aria-hidden="true"><circle cx="8" cy="8" r="6" fill="none" stroke="#fff" stroke-width="2.4"/><line x1="12.5" y1="12.5" x2="18" y2="18" stroke="#fff" stroke-width="2.6"/></svg>
</nav>
<h1 class="abs hero-name"><span>Dane</span><span>Whitfield</span></h1>
<div class="abs hero-bar"><p>LIVE LIFE ON YOUR TERMS</p></div>

<section class="abs offer" role="img" aria-label="Teal sky fading to sunset with a hiker standing on a rock"></section>
<div class="abs offer-figure" role="img" aria-label="Silhouette of a hiker on a rock"></div>
<h2 class="abs offer-title">I am giving away everything<br>that I know for free.</h2>
<div class="abs btn-signup">Sign up now</div>
<div class="abs promo promo-meet" role="img" aria-label="Black and white portrait of Dane">Meet Dane Whitfield</div>
<div class="abs promo promo-opp" role="img" aria-label="Dane under palm trees">Opportunities don't happen. You create them.</div>
<div class="abs promo promo-course" role="img" aria-label="Dusky purple sky">Live life on your terms with my free Course</div>

<div class="abs bio-box"></div>
<div class="abs avatar" role="img" aria-label="Round portrait of Dane on a cyan background"></div>
<svg class="abs trophy" width="80" height="80" viewBox="0 0 80 80" aria-hidden="true">
  <path d="M20 8h40v20c0 14-9 24-20 24S20 42 20 28z" fill="#2aa9a0"/>
  <path d="M20 14H8c0 12 6 20 14 20M60 14h12c0 12-6 20-14 20" fill="none" stroke="#2aa9a0" stroke-width="5"/>
  <rect x="35" y="50" width="10" height="12" fill="#2aa9a0"/>
  <rect x="24" y="62" width="32" height="9" fill="#2aa9a0"/>
</svg>
<div class="abs bio-box-text">
  <p>Dane Whitfield is a 7 figure Ecommerce Entrepreneur, Speaker, Inventor, Bio-hacker, and Positive thinker. He believes the world is getting better every day.</p>
  <p>Dane went from 0 to 6 Million in 6 Months selling Eclipse Glasses on Marketly FBM. He also proposed to his wife in Outer Space. He is not your typical person</p>
</div>
<div class="abs stat">
  <h2>From 0 to 6</h2>
  <h3>Million</h3>
  <hr>
  <p>in 6 Months selling Eclipse<br>Glasses on Marketly FBM</p>
</div>
<div class="abs join-sellers" role="img" aria-label="Person with arms raised before a waterfall and rainbow"><p>Join 40,000+<br>Marketly Sellers.</p></div>

<h2 class="abs posts-title">Recent posts</h2>
<p class="abs posts-sub">Keep going. Start chasing the passion.</p>
<div class="abs video row1 c1" role="img" aria-label="Video thumbnail"><span class="title">Launch Tools Product Discovery Compared</span><span class="play"></span></div>
<div class="abs video green row1 c2" role="img" aria-label="Video thumbnail"><span class="title">How Much MONEY Do You Need To Start</span><span class="play"></span></div>
<div class="abs video yellow row1 c3" role="img" aria-label="Video thumbnail"><span class="title">Marketly FBM PRODUCT RESEARCH Mistakes</span><span class="play"></span></div>
<div class="abs video row2 c1" role="img" aria-label="Video thumbnail"><span class="title">Launch Tools Product Discovery Compared</span><span class="play"></span></div>
<div class="abs video green row2 c2" role="img" aria-label="Video thumbnail"><span class="title">How Much MONEY Do You Need To Start</span><span class="play"></span></div>
<div class="abs video yellow row2 c3" role="img" aria-label="Video thumbnail"><span class="title">Marketly FBM PRODUCT RESEARCH Mistakes</span><span class="play"></span></div>

<div class="abs testi-bg" role="img" aria-label="Soft grey smoke texture"></div>
<h2 class="abs testi-title">Testimonials</h2>
<p class="abs testi-lead">Ut ultricies imperdiet sodales.<br>Aliquam fringilla aliquam ex sit amet elementum.</p>
<div class="abs quote q1"><span class="face face-a" role="img" aria-label="Reviewer portrait"></span><blockquote>Vitae adipiscing turpis. Aenean ligula nibh, molestie id viverra a, dapibus at dolor. In iaculis viverra</blockquote><cite>Tomas Kerrigan</cite></div>
<div class="abs quote q2"><span class="face face-b" role="img" aria-label="Reviewer portrait"></span><blockquote>Vitae adipiscing turpis. Aenean ligula nibh, molestie id viverra a, dapibus at dolor. In iaculis viverra</blockquote><cite>Selina Varga</cite></div>
<div class="abs quote q3"><span class="face face-c" role="img" aria-label="Reviewer portrait"></span><blockquote>Vitae adipiscing turpis. Aenean ligula nibh, molestie id viverra a, dapibus at dolor. In iaculis viverra</blockquote><cite>Tomas Kerrigan</cite></div>

<section class="abs community"><p>Join Dane &amp; his 20,000+ Community on VidStream</p><span class="btn-join">Join now</span></section>

<footer class="abs footer"></footer>
<div class="abs footer-brand">Dane Whitfield</div>
<div class="abs footer-col col-about">
  <h4>About:</h4>
  <p>Aenean luctus, neque et interdum efficitur, magna enim porttitor tellus.</p>
  <p>Vitae finibus turpis et tellus. Nullam pellentesque venenatis neque, in congue diam iaculis eget. Phasellus fermentum velit sed libero vitae finibus tortor consectetur.</p>
</div>
<div class="abs footer-col col-contact">
  <h4>Contact:</h4>
  <p>North Branch - tel. 0700 000 101<br>East Branch - tel. 0700 000 102<br>Send us your offers and availability:<br>hello@danewhitfield.example</p>
  <p>Central office - 12 Mill Street, tel. 0700 000 103<br>South office - 4 Harbour Road, tel. 0700 000 104</p>
</div>
<div class="abs footer-col col-follow">
  <h4>Follow me:</h4>
  <div class="social"><span></span><span></span><span></span><span></span></div>
</div>
<p class="abs copyright">© 2018 Dane Whitfield - All Rights Reserved.</p>

</body>
</html>
```